CD cover/promotional graphic for a new single

I had this up as a project already and I decided to change the image and start a new campaign. So, please use this image and manipulate it whatever way you want, however I’m looking for something impactful, in your face, and mind blowing. Please include the title ‘Quiet Harbor Drift’ and the artist ‘Marcus Pellworth’ on it. Extra points if you can add a tad more burnout smoke in a tasteful way. I’ve also attached the song. Thank you.

```html
<!DOCTYPE html>
<html lang="en">
<head>
<meta charset="utf-8">
<title>Quiet Harbor Drift – Single Cover Versions</title>
<link rel="stylesheet" href="https://fonts.googleapis.com/css2?family=Racing+Sans+One&family=Oswald:wght@500;700&family=Roboto:wght@300&display=swap">
<style>
  :root {
    --page: #ffffff;
    --label: #7a7a7a;
    --sky-top: #1f8fc6;
    --sky-mid: #6fb4d6;
    --horizon: #c9b59a;
    --ground: #5a3a2c;
    --ground-dark: #2d2320;
    --car-red: #b3222a;
    --ink-white: #ffffff;
    --fine-ink: #f2f2f2;
    --v1-title: #f5ea12;
    --v2-title-top: #ffd23a;
    --v2-title-bottom: #ef5a12;
    --v3-title-top: #e0193d;
    --v3-chrome-light: #d9f1fb;
    --v3-chrome-dark: #2f7fa6;
    --disc-rim: #c9ccd0;
    --hub-light: #d8dade;
    --hub-dark: #6e7378;
    --case-edge: #d6d8da;
    --case-spine: #1b1b1b;
  }
  * { margin: 0; padding: 0; box-sizing: border-box; }
  html, body { width: 1200px; height: 2280px; overflow: hidden; background: var(--page); }
  .sheet { position: relative; width: 1200px; height: 2280px; }

  .version { position: absolute; left: 0; width: 1200px; height: 726px; }
  .version--one { top: 0; }
  .version--two { top: 722px; }
  .version--three { top: 1450px; }

  .version-label {
    position: absolute; left: 40px; top: 36px;
    font: 300 23px/1 "Roboto", sans-serif; color: var(--label);
  }

  .disc { position: absolute; left: 593px; top: 130px; width: 580px; height: 580px; z-index: 1; }
  .disc text { font-family: "Racing Sans One", sans-serif; }
  .disc .disc-artist { font-family: "Oswald", sans-serif; font-weight: 700; font-style: italic; letter-spacing: 2px; }
  .disc .disc-fine { font-family: "Oswald", sans-serif; font-weight: 500; letter-spacing: 0.4px; }

  .jewel-case {
    position: absolute; left: 48px; top: 126px; width: 674px; height: 600px;
    background: #eef0f1; border: 2px solid var(--case-edge); z-index: 2;
  }
  .case-spine {
    position: absolute; left: 6px; top: 8px; width: 38px; bottom: 8px;
    background: var(--case-spine);
  }
  .cover {
    position: absolute; left: 44px; top: 8px; width: 620px; height: 580px;
    overflow: hidden;
  }
  .cover-photo {
    position: absolute; inset: 0;
    background:
      radial-gradient(ellipse 46% 26% at 42% 58%, var(--car-red) 0 60%, transparent 100%),
      linear-gradient(180deg, var(--sky-top) 0%, var(--sky-mid) 38%, var(--horizon) 52%, var(--ground) 68%, var(--ground-dark) 100%);
  }
  .version--two .cover-photo {
    background:
      radial-gradient(ellipse 46% 26% at 42% 58%, var(--car-red) 0 60%, transparent 100%),
      radial-gradient(ellipse 50% 18% at 60% 78%, rgba(255,140,30,.55), transparent 100%),
      linear-gradient(180deg, var(--sky-top) 0%, var(--sky-mid) 38%, var(--horizon) 52%, var(--ground) 68%, var(--ground-dark) 100%);
  }
  .version--three .cover-photo {
    background:
      radial-gradient(ellipse 46% 26% at 42% 58%, var(--car-red) 0 60%, transparent 100%),
      radial-gradient(ellipse 50% 18% at 60% 80%, rgba(240,40,70,.45), transparent 100%),
      linear-gradient(180deg, #2aa6e8 0%, #8fd0ef 38%, var(--horizon) 52%, var(--ground) 68%, var(--ground-dark) 100%);
  }

  .cover-title {
    position: absolute; left: 80px; top: 40px; width: 500px;
    font-family: "Racing Sans One", sans-serif; font-weight: 400; line-height: .82;
    transform: rotate(-4deg); transform-origin: left top;
  }
  .title-top { display: block; font-size: 62px; }
  .title-main { display: block; font-size: 164px; margin-left: -4px; }

  .version--one .title-top, .version--one .title-main { color: var(--v1-title); }
  .version--two .title-top, .version--two .title-main {
    background: linear-gradient(180deg, var(--v2-title-top), var(--v2-title-bottom));
    -webkit-background-clip: text; background-clip: text; color: transparent;
  }
  .version--three .title-top { color: var(--v3-title-top); }
  .version--three .title-main {
    background: linear-gradient(180deg, var(--v3-chrome-light) 0%, #8fc9e2 45%, var(--v3-chrome-dark) 55%, #bfe6f4 100%);
    -webkit-background-clip: text; background-clip: text; color: transparent;
  }

  .cover-artist {
    position: absolute; left: 0; right: 0; top: 428px; text-align: center;
    font-family: "Oswald", sans-serif; font-style: italic; color: var(--ink-white);
  }
  .artist-label { display: block; font-weight: 500; font-size: 16px; letter-spacing: 6px; text-transform: uppercase; }
  .artist-name { display: block; font-weight: 700; font-size: 26px; letter-spacing: 3px; margin-top: 2px; }

  .cover-fine {
    position: absolute; left: 140px; right: 140px; top: 534px; text-align: center;
    font: 500 7.5px/1.45 "Oswald", sans-serif; letter-spacing: .6px; color: var(--fine-ink);
    text-transform: uppercase;
  }
</style>
</head>
<body>
<main class="sheet">

  <section class="version version--one">
    <p class="version-label">CD Cover Design - Revised Version 1</p>
    <svg class="disc" viewBox="0 0 580 580" aria-label="Disc label, version 1">
      <defs>
        <clipPath id="disc-clip-1"><circle cx="290" cy="290" r="288"/></clipPath>
        <linearGradient id="disc-bg-1" x1="0" y1="0" x2="0" y2="1">
          <stop offset="0" stop-color="#1c7fb0"/><stop offset=".55" stop-color="#7ab8d6"/>
          <stop offset=".72" stop-color="#b06050"/><stop offset="1" stop-color="#3a2a24"/>
        </linearGradient>
      </defs>
      <g clip-path="url(#disc-clip-1)">
        <rect width="580" height="580" fill="url(#disc-bg-1)" role="img" aria-label="Red muscle car doing a burnout with blue light trails and smoke"/>
        <text x="140" y="100" font-size="40" fill="#f5ea12" transform="rotate(-3 140 100)">Quiet Harbor</text>
        <text x="136" y="180" font-size="90" fill="#f5ea12" transform="rotate(-3 136 180)">Drift</text>
        <text class="disc-artist" x="136" y="252" font-size="14" fill="#fff">PELLWORTH</text>
        <g class="disc-fine" font-size="7" fill="#fff" text-anchor="middle">
          <text x="470" y="278">TURN IT UP AND LET THE</text>
          <text x="470" y="288">ENGINE SING ALONG. PRODUCED,</text>
          <text x="470" y="298">MIXED AND MASTERED</text>
          <text x="470" y="308">FOR THE OPEN</text>
          <text x="470" y="318">ROAD.</text>
        </g>
      </g>
      <circle cx="290" cy="290" r="84" fill="var(--hub-dark)"/>
      <circle cx="290" cy="290" r="72" fill="var(--hub-light)"/>
      <circle cx="290" cy="290" r="52" fill="#9aa0a6"/>
      <circle cx="290" cy="290" r="32" fill="var(--page)"/>
      <circle cx="290" cy="290" r="288" fill="none" stroke="var(--disc-rim)" stroke-width="4"/>
    </svg>
    <div class="jewel-case">
      <div class="case-spine"></div>
      <div class="cover">
        <div class="cover-photo" role="img" aria-label="Red muscle car doing a burnout on a desert road, blue and yellow light trails and tyre smoke under a cloudy sky"></div>
        <h1 class="cover-title"><span class="title-top">Quiet Harbor</span><span class="title-main">Drift</span></h1>
        <p class="cover-artist"><span class="artist-label">Artist</span><span class="artist-name">MARCUS PELLWORTH</span></p>
        <p class="cover-fine">New single available now on every major streaming platform. Recorded live at the Harbor Room studio with the full road band. Mixed loud for open windows and late night drives.</p>
      </div>
    </div>
  </section>

  <section class="version version--two">
    <p class="version-label">CD Cover Design - Revised Version 2</p>
    <svg class="disc" viewBox="0 0 580 580" aria-label="Disc label, version 2">
      <defs>
        <clipPath id="disc-clip-2"><circle cx="290" cy="290" r="288"/></clipPath>
        <linearGradient id="disc-bg-2" x1="0" y1="0" x2="0" y2="1">
          <stop offset="0" stop-color="#1c7fb0"/><stop offset=".55" stop-color="#7ab8d6"/>
          <stop offset=".72" stop-color="#c06040"/><stop offset="1" stop-color="#3a2a24"/>
        </linearGradient>
        <linearGradient id="disc-title-2" x1="0" y1="0" x2="0" y2="1">
          <stop offset="0" stop-color="#ffd23a"/><stop offset="1" stop-color="#ef5a12"/>
        </linearGradient>
      </defs>
      <g clip-path="url(#disc-clip-2)">
        <rect width="580" height="580" fill="url(#disc-bg-2)" role="img" aria-label="Red muscle car doing a burnout with orange light trails and smoke"/>
        <text x="140" y="100" font-size="40" fill="url(#disc-title-2)" transform="rotate(-3 140 100)">Quiet Harbor</text>
        <text x="136" y="180" font-size="90" fill="url(#disc-title-2)" transform="rotate(-3 136 180)">Drift</text>
        <text class="disc-artist" x="136" y="252" font-size="14" fill="#fff">PELLWORTH</text>
        <g class="disc-fine" font-size="7" fill="#fff" text-anchor="middle">
          <text x="470" y="278">TURN IT UP AND LET THE</text>
          <text x="470" y="288">ENGINE SING ALONG. PRODUCED,</text>
          <text x="470" y="298">MIXED AND MASTERED</text>
          <text x="470" y="308">FOR THE OPEN</text>
          <text x="470" y="318">ROAD.</text>
        </g>
      </g>
      <circle cx="290" cy="290" r="84" fill="var(--hub-dark)"/>
      <circle cx="290" cy="290" r="72" fill="var(--hub-light)"/>
      <circle cx="290" cy="290" r="52" fill="#9aa0a6"/>
      <circle cx="290" cy="290" r="32" fill="var(--page)"/>
      <circle cx="290" cy="290" r="288" fill="none" stroke="var(--disc-rim)" stroke-width="4"/>
    </svg>
    <div class="jewel-case">
      <div class="case-spine"></div>
      <div class="cover">
        <div class="cover-photo" role="img" aria-label="Red muscle car doing a burnout on a desert road, orange fire-coloured light trails and tyre smoke under a cloudy sky"></div>
        <h1 class="cover-title"><span class="title-top">Quiet Harbor</span><span class="title-main">Drift</span></h1>
        <p class="cover-artist"><span class="artist-label">Artist</span><span class="artist-name">MARCUS PELLWORTH</span></p>
        <p class="cover-fine">New single available now on every major streaming platform. Recorded live at the Harbor Room studio with the full road band. Mixed loud for open windows and late night drives.</p>
      </div>
    </div>
  </section>

  <section class="version version--three">
    <p class="version-label">CD Cover Design - Revised Version 3</p>
    <svg class="disc" viewBox="0 0 580 580" aria-label="Disc label, version 3">
      <defs>
        <clipPath id="disc-clip-3"><circle cx="290" cy="290" r="288"/></clipPath>
        <linearGradient id="disc-bg-3" x1="0" y1="0" x2="0" y2="1">
          <stop offset="0" stop-color="#1e9be0"/><stop offset=".55" stop-color="#8fd0ef"/>
          <stop offset=".72" stop-color="#b05058"/><stop offset="1" stop-color="#3a2a24"/>
        </linearGradient>
        <linearGradient id="disc-chrome-3" x1="0" y1="0" x2="0" y2="1">
          <stop offset="0" stop-color="#d9f1fb"/><stop offset=".45" stop-color="#8fc9e2"/>
          <stop offset=".55" stop-color="#2f7fa6"/><stop offset="1" stop-color="#bfe6f4"/>
        </linearGradient>
      </defs>
      <g clip-path="url(#disc-clip-3)">
        <rect width="580" height="580" fill="url(#disc-bg-3)" role="img" aria-label="Red muscle car doing a burnout with red and teal light trails and smoke"/>
        <text x="140" y="100" font-size="40" fill="#e0193d" transform="rotate(-3 140 100)">Quiet Harbor</text>
        <text x="136" y="180" font-size="90" fill="url(#disc-chrome-3)" transform="rotate(-3 136 180)">Drift</text>
        <text class="disc-artist" x="136" y="252" font-size="14" fill="#fff">PELLWORTH</text>
        <g class="disc-fine" font-size="7" fill="#fff" text-anchor="middle">
          <text x="470" y="278">TURN IT UP AND LET THE</text>
          <text x="470" y="288">ENGINE SING ALONG. PRODUCED,</text>
          <text x="470" y="298">MIXED AND MASTERED</text>
          <text x="470" y="308">FOR THE OPEN</text>
          <text x="470" y="318">ROAD.</text>
        </g>
      </g>
      <circle cx="290" cy="290" r="84" fill="var(--hub-dark)"/>
      <circle cx="290" cy="290" r="72" fill="var(--hub-light)"/>
      <circle cx="290" cy="290" r="52" fill="#9aa0a6"/>
      <circle cx="290" cy="290" r="32" fill="var(--page)"/>
      <circle cx="290" cy="290" r="288" fill="none" stroke="var(--disc-rim)" stroke-width="4"/>
    </svg>
    <div class="jewel-case">
      <div class="case-spine"></div>
      <div class="cover">
        <div class="cover-photo" role="img" aria-label="Red muscle car doing a burnout on a desert road, red and teal light trails and tyre smoke under a bright cloudy sky"></div>
        <h1 class="cover-title"><span class="title-top">Quiet Harbor</span><span class="title-main">Drift</span></h1>
        <p class="cover-artist"><span class="artist-label">Artist</span><span class="artist-name">MARCUS PELLWORTH</span></p>
        <p class="cover-fine">New single available now on every major streaming platform. Recorded live at the Harbor Room studio with the full road band. Mixed loud for open windows and late night drives.</p>
      </div>
    </div>
  </section>

</main>
</body>
</html>
```